Pull up display banner design for cloud hosting company

Our company is called BrightPebble NetServe and we are sponsoring an innovative business startup weekend. We want to attract young and budding entrepreneurs as new clients.

We requirement a display banner to be designed to be placed at the front of the room next to the speaker for all to see. It should be a single sided design for a pullup banner 85cm x 200cm at 300dpi resolution in PSD, AI and PDF Format. I have upload the logo and can provide other images if required from the site.

We want to offer these young and budding entrepreneurs flexible, reliable and scalable hosting solutions for their websites, communication, collaboration and business apps. We want people to feel like they are dealing with 'real' people that are living an entrepreneurial lifestyle in our workplace http://brightpebbleserve.com.au/newsite/why/doing-it-different (access details below)

website is located here www.brightpebbleserve.com.au/newsite
username: demoarea
Password: Sample789
Although the website on the banner would be www.brightpebbleserve.com.au
Phone - 1300 PEBBLES (1300 732 253)

BrightPebble NetServe is a Cloud Hosting provider. We differentiate ourselves by focusing on:

Eco friendly / carbon neutral infrastructure
Contributions to positive change projects through our BrightPebble Fund
Personal and understanding customer service
Highly redundant business class hosting
Fully managed custom solutions - VPS's, DNS, Backups, Monitoring
Business Apps
Strong relationships with our Partner Allied Network

Target Market(s)

young and budding entrepreneurs

Industry/Entity Type

Business

Requirements
Must have
• website
contact phone
list of services
trademark - 'Servers for a kinder planet'
Some sort of a carbon neutral/eco friendly symbol

```html
<!DOCTYPE html>
<html lang="en">
<head>
<meta charset="utf-8">
<title>BrightPebble NetServe – Pull Up Banner</title>
<link href="https://fonts.googleapis.com/css2?family=Raleway:wght@300;400;500&family=Comfortaa:wght@400;700&display=swap" rel="stylesheet">
<style>
  :root {
    --paper: #ffffff;
    --ink: #3a3a3a;
    --ink-soft: #5a5a5a;
    --teal: #2fb3c6;
    --green: #7cb82a;
    --eco-green: #6cb33f;
    --photo-warm: #e4d8cc;
    --photo-grey: #c9c9c9;
  }
  * { margin: 0; padding: 0; box-sizing: border-box; }
  html, body { width: 1200px; height: 2527px; overflow: hidden; background: var(--paper); }
  .banner {
    position: relative;
    width: 1200px;
    height: 2527px;
    overflow: hidden;
    background: var(--paper);
    font-family: "Raleway", sans-serif;
    color: var(--ink);
  }
  .headline {
    position: absolute;
    left: 70px;
    top: 1850px;
    transform: rotate(-90deg);
    transform-origin: left top;
    white-space: nowrap;
    font-family: "Comfortaa", sans-serif;
    font-weight: 400;
    font-size: 110px;
    line-height: 130px;
    letter-spacing: 1px;
    color: var(--ink);
  }
  .headline .brand-word { color: var(--teal); }

  .column {
    position: absolute;
    left: 300px;
    width: 820px;
    text-align: center;
    white-space: nowrap;
  }
  .crowd-photo {
    top: 30px;
    left: 410px;
    width: 600px;
    height: 450px;
    border-radius: 50% 50% 45% 45%;
    background: radial-gradient(ellipse at 50% 45%, var(--photo-warm) 0%, #d6c6b6 55%, rgba(255,255,255,0) 72%);
  }
  .equation-word {
    top: 500px;
    font-size: 56px;
    letter-spacing: 4px;
    color: var(--ink-soft);
  }
  .operator {
    top: 560px;
    font-family: "Comfortaa", sans-serif;
    font-weight: 700;
    font-size: 130px;
    line-height: 130px;
    color: var(--green);
  }
  .operator.equals { top: 880px; }
  .brand-mark {
    top: 760px;
    font-family: "Comfortaa", sans-serif;
    font-size: 62px;
    line-height: 80px;
    color: var(--ink);
  }
  .dot {
    display: inline-block;
    border-radius: 50%;
    background: var(--teal);
    vertical-align: middle;
  }
  .brand-mark .dot { width: 32px; height: 32px; margin-right: 16px; }
  .plant-photo {
    top: 1020px;
    left: 470px;
    width: 480px;
    height: 360px;
    border-radius: 40% 40% 30% 30%;
    background: radial-gradient(ellipse at 50% 55%, #9c9c9c 0%, var(--photo-grey) 45%, rgba(255,255,255,0) 72%);
  }
  .tagline {
    top: 1400px;
    font-size: 44px;
    line-height: 56px;
    letter-spacing: 2px;
    text-transform: uppercase;
    color: var(--ink);
  }

  .services {
    position: absolute;
    top: 1570px;
    left: 320px;
    width: 840px;
    display: flex;
    justify-content: space-between;
  }
  .service { width: 200px; text-align: center; }
  .service-label {
    height: 90px;
    font-size: 27px;
    line-height: 32px;
    text-transform: uppercase;
    color: var(--ink-soft);
  }
  .service-icon { height: 150px; display: flex; align-items: center; justify-content: center; }
  .at-sign { font-size: 120px; color: #222; line-height: 1; }

  .eco-badge { position: absolute; left: 70px; top: 1900px; }

  .footer-brand {
    position: absolute;
    top: 2110px;
    left: 300px;
    width: 820px;
    text-align: center;
    white-space: nowrap;
    font-family: "Comfortaa", sans-serif;
    font-size: 66px;
    line-height: 90px;
    color: var(--ink);
  }
  .footer-brand .dot { width: 36px; height: 36px; margin-right: 16px; }
  .phone {
    position: absolute;
    top: 2280px;
    left: 320px;
    white-space: nowrap;
    font-size: 52px;
    letter-spacing: 2px;
    color: var(--ink);
  }
  .web {
    position: absolute;
    top: 2370px;
    left: 320px;
    white-space: nowrap;
    font-size: 48px;
    letter-spacing: 1px;
    color: var(--ink);
  }
  .web .domain { color: var(--teal); }
</style>
</head>
<body>
<main class="banner">
  <h1 class="headline">Why Choose <span class="brand-word">BrightPebble?</span></h1>

  <div class="column crowd-photo" role="img" aria-label="Photo of a cheerful group of young people raising their arms, seen from above"></div>

  <p class="column equation-word">YOU</p>
  <p class="column operator plus">+</p>
  <p class="column brand-mark"><span class="dot"></span>BrightPebble</p>
  <p class="column operator equals">=</p>

  <div class="column plant-photo" role="img" aria-label="Black and white photo of cupped hands holding soil with a green seedling"></div>
  <p class="column tagline">Servers for<br>a kinder planet</p>

  <svg class="eco-badge" width="150" height="150" viewBox="0 0 150 150" role="img" aria-label="Eco friendly symbol">
    <path d="M75 138 C30 105 8 80 8 50 C8 26 26 10 47 10 C60 10 70 17 75 28 C80 17 90 10 103 10 C124 10 142 26 142 50 C142 80 120 105 75 138 Z" fill="var(--eco-green)"/>
  </svg>

  <section class="services">
    <div class="service">
      <p class="service-label">Global<br>Domains</p>
      <div class="service-icon"><span class="at-sign">@</span></div>
    </div>
    <div class="service">
      <p class="service-label">Website<br>Hosting</p>
      <div class="service-icon">
        <svg width="150" height="130" viewBox="0 0 150 130">
          <rect x="5" y="5" width="140" height="90" rx="6" fill="#2a2a2a"/>
          <rect x="13" y="13" width="124" height="74" fill="var(--teal)"/>
          <text x="75" y="60" text-anchor="middle" font-family="Raleway, sans-serif" font-size="28" font-weight="500" fill="#ffffff">www.</text>
          <rect x="65" y="95" width="20" height="18" fill="#555"/>
          <rect x="40" y="113" width="70" height="8" rx="3" fill="#777"/>
        </svg>
      </div>
    </div>
    <div class="service">
      <p class="service-label">Custom<br>Cloud/VPS</p>
      <div class="service-icon">
        <svg width="170" height="130" viewBox="0 0 170 130">
          <defs>
            <linearGradient id="cloudFill" x1="0" y1="0" x2="0" y2="1">
              <stop offset="0" stop-color="#7fd0ee"/>
              <stop offset="1" stop-color="#1c7fc0"/>
            </linearGradient>
          </defs>
          <path d="M40 115 C15 115 5 98 5 82 C5 64 20 52 38 54 C42 30 62 15 85 15 C110 15 128 32 131 55 C152 55 165 70 165 86 C165 103 152 115 132 115 Z" fill="url(#cloudFill)"/>
          <rect x="60" y="55" width="60" height="55" rx="6" fill="#3a3a3a"/>
          <rect x="68" y="64" width="44" height="8" fill="#888"/>
          <rect x="68" y="78" width="44" height="8" fill="#888"/>
          <rect x="68" y="92" width="44" height="8" fill="#888"/>
        </svg>
      </div>
    </div>
    <div class="service">
      <p class="service-label">Business<br>App's</p>
      <div class="service-icon">
        <svg width="170" height="130" viewBox="0 0 170 130" stroke="#444" stroke-width="2" fill="none">
          <rect x="68" y="10" width="34" height="34" rx="6" fill="#333"/>
          <circle cx="85" cy="27" r="8" stroke="#fff"/>
          <path d="M85 44 V70 M25 70 H145 M25 70 V92 M65 70 V92 M105 70 V92 M145 70 V92"/>
          <rect x="12" y="92" width="26" height="20" fill="#fff"/>
          <rect x="54" y="92" width="22" height="28" fill="#fff"/>
          <rect x="94" y="92" width="24" height="20" fill="#fff"/>
          <rect x="136" y="92" width="18" height="28" fill="#fff"/>
        </svg>
      </div>
    </div>
  </section>

  <p class="footer-brand"><span class="dot"></span>BrightPebble NetServe</p>
  <p class="phone">1300 PEBBLES (1300 732 253)</p>
  <p class="web">www.<span class="domain">brightpebbleserve</span>.com.au</p>
</main>
</body>
</html>
```